Moravel Stenwick Inc needs a business card design

Looking for a unique, classy and sharp business card design.

Contact Information for Business Card

Moravel Stenwick Inc.
Marisa Ortega Bellido BScOT(c)
Occupational Therapist
(780) 555-0142
moravelstenwick@postlynx.net

```html
<!DOCTYPE html>
<html lang="en">
<head>
<meta charset="utf-8">
<title>Moravel Stenwick Inc. – Business Card</title>
<link href="https://fonts.googleapis.com/css2?family=Open+Sans:wght@400;700&display=swap" rel="stylesheet">
<style>
  :root {
    --backdrop: #e6e8ec;
    --card: #ffffff;
    --brand-purple: #922a91;
    --brand-green: #8cc63f;
    --ink: #1f1f1f;
    --on-purple: #ffffff;
  }
  * { box-sizing: border-box; margin: 0; padding: 0; }
  html, body {
    width: 1200px;
    height: 854px;
    overflow: hidden;
    background: var(--backdrop);
    font-family: "Open Sans", Arial, sans-serif;
  }
  .business-card {
    position: absolute;
    left: 150px;
    top: 170px;
    width: 900px;
    height: 514px;
    background: var(--card);
    box-shadow: 0 10px 30px rgba(0,0,0,0.18);
  }
  .name-band {
    position: absolute;
    left: 0;
    top: 86px;
    width: 540px;
    height: 100px;
    background: var(--brand-purple);
    color: var(--on-purple);
    padding: 14px 0 0 62px;
  }
  .name-band__name {
    font-size: 33px;
    font-weight: 700;
    line-height: 1.15;
    white-space: nowrap;
  }
  .name-band__credential {
    font-size: 22px;
    font-weight: 400;
    margin-left: 4px;
  }
  .name-band__title {
    font-size: 24px;
    font-weight: 400;
    line-height: 1.3;
  }
  .brand-mark {
    position: absolute;
    right: 56px;
    top: 150px;
    width: 300px;
    display: flex;
    flex-direction: column;
    align-items: center;
    gap: 16px;
  }
  .brand-mark__dot {
    width: 64px;
    height: 64px;
    border-radius: 50%;
    background: var(--brand-green);
  }
  .brand-mark__name {
    font-size: 34px;
    font-weight: 700;
    color: var(--brand-purple);
    text-align: center;
    line-height: 1.15;
  }
  .contact-list {
    position: absolute;
    left: 62px;
    bottom: 72px;
    list-style: none;
    font-size: 24px;
    color: var(--ink);
  }
  .contact-list__item {
    display: flex;
    align-items: center;
    gap: 16px;
    line-height: 1.6;
  }
  .contact-list__icon {
    width: 22px;
    height: 22px;
    fill: var(--brand-purple);
    flex: none;
  }
</style>
</head>
<body>
  <article class="business-card">
    <header class="name-band">
      <p class="name-band__name">Marisa Ortega Bellido<span class="name-band__credential">BScOT(c)</span></p>
      <p class="name-band__title">Occupational Therapist</p>
    </header>

    <div class="brand-mark">
      <span class="brand-mark__dot"></span>
      <p class="brand-mark__name">Moravel Stenwick Inc.</p>
    </div>

    <ul class="contact-list">
      <li class="contact-list__item">
        <svg class="contact-list__icon" viewBox="0 0 24 24" aria-hidden="true">
          <path d="M6.6 10.8a15.1 15.1 0 0 0 6.6 6.6l2.2-2.2a1 1 0 0 1 1-.25 11.4 11.4 0 0 0 3.6.57 1 1 0 0 1 1 1V20a1 1 0 0 1-1 1A17 17 0 0 1 3 4a1 1 0 0 1 1-1h3.5a1 1 0 0 1 1 1c0 1.25.2 2.45.57 3.6a1 1 0 0 1-.25 1z"/>
        </svg>
        <span>(780) 555-0142</span>
      </li>
      <li class="contact-list__item">
        <svg class="contact-list__icon" viewBox="0 0 24 24" aria-hidden="true">
          <path d="M2 5h20v14H2z M2 5l10 8 10-8" fill="none" stroke="var(--brand-purple)" stroke-width="0"/>
          <path d="M2 6.2V19h20V6.2l-10 7.6z M3 5l9 6.8L21 5z"/>
        </svg>
        <span>moravelstenwick@postlynx.net</span>
      </li>
    </ul>
  </article>
</body>
</html>
```